Need Website for PR Firm

I need a website for my new business, Lantern Hill Agency, a PR, Communications and Marketing Firm. I want something classy and clean. Tailored and professional with a bit of a whimsical touch. Colors are mainly white and green. I don't like random stock photos but I would consider an image of a park with the city in the background. The name of my company is a play on Willowmere Green in Brooklyn where I am based.

The navigation and pages I will need is a good clean landing page.
About us
Who we are
Contact

Again, I like clean white and the copy in a similar color and font as my logo.
No stock photography or clip art.
I uploaded an image of the park that I like and wld be open to using in some way
Updates

I have uploaded an image of the park that you could implemented. 

Seeing some good designs here.

With the image I uploaded, I unfortunately think the green sky is too green.
Wondering if we can make modifications to the color of the sky.
I like the last image submitted too.

Target Market(s)

Professionals and the media who are seeing how I represent myself and my agency as they hire me for the public relations council.

Industry/Entity Type

Business

Font styles to use
Serif
Other font styles liked:
• Trajan

Colors
acd036
ffffff
dbdbdb
eeeeee

Requirements
Must have
• High quality and consistent colors and font.
Should not have
• Stock photography
Clip art
colors that aren't white, the green in my font, black or gray if necessary.

```html
<!DOCTYPE html>
<html lang="en">
<head>
<meta charset="utf-8">
<title>Lantern Hill Agency</title>
<link href="https://fonts.googleapis.com/css2?family=Cinzel:wght@400;700&family=Open+Sans:wght@400;600;700&display=swap" rel="stylesheet">
<style>
:root{
  --green:#acd036;
  --green-dark:#93b524;
  --white:#ffffff;
  --light:#eeeeee;
  --mid:#dbdbdb;
  --grey:#8a8a8a;
  --text:#555555;
  --dark:#333333;
  --teal:#2aa3c4;
}
*{margin:0;padding:0;box-sizing:border-box}
html,body{width:677px;height:1200px;overflow:hidden;background:var(--white)}
body{font-family:"Open Sans",Arial,sans-serif;color:var(--text);font-size:7px;line-height:1.5;position:relative}

/* header */
.site-header{position:absolute;top:0;left:0;width:677px;height:65px}
.brand{position:absolute;left:26px;top:14px;display:flex;align-items:center;gap:7px}
.brand-square{width:22px;height:22px;background:var(--green);flex:none}
.brand-name{font-family:"Cinzel",Georgia,serif;color:var(--green);font-size:13px;line-height:1.05;font-weight:700;width:120px}
.client-login{position:absolute;right:30px;top:4px;background:var(--green);color:var(--white);font-size:6px;font-weight:700;padding:3px 9px;letter-spacing:.5px;border-radius:2px}
.main-nav{position:absolute;top:42px;left:240px;display:flex;gap:2px;align-items:center}
.main-nav a{font-size:8px;color:var(--text);text-decoration:none;padding:4px 8px}
.main-nav a.active{background:var(--green);color:var(--white)}
.search{margin-left:10px;width:78px;height:15px;border:1px solid var(--mid);font-size:6px;color:var(--grey);padding:3px 5px}

/* hero */
.hero{position:absolute;top:65px;left:0;width:677px;height:280px;
  background:linear-gradient(180deg,#9fc3dd 0%,#c9dce8 30%,#8ea7a0 50%,#c7c1ae 65%,#4f86a3 80%,#3d7495 100%)}
.hero-caption{position:absolute;right:58px;top:108px;width:190px;color:var(--white);font-family:"Cinzel",Georgia,serif;font-size:10px;line-height:1.35;font-weight:700;letter-spacing:.3px}
.hero-btn{display:inline-block;margin-top:8px;background:var(--green);color:var(--white);font-family:"Open Sans",sans-serif;font-size:6px;padding:4px 10px}
.hero-dots{position:absolute;bottom:12px;left:50%;transform:translateX(-50%);display:flex;gap:5px}
.hero-dots span{width:5px;height:5px;border-radius:50%;background:rgba(255,255,255,.6)}
.hero-dots span.on{background:var(--green)}
.support-tab{position:absolute;left:0;top:245px;width:14px;height:50px;background:var(--teal);color:var(--white);font-size:6px;font-weight:700;writing-mode:vertical-rl;transform:rotate(180deg);text-align:center;line-height:14px}

/* who we are */
.who{position:absolute;top:355px;left:60px;width:557px;text-align:center}
.section-title{font-family:"Cinzel",Georgia,serif;font-size:16px;color:var(--dark);letter-spacing:1px}
.who p{margin-top:8px;font-size:7px;color:var(--text)}

/* what we do */
.what{position:absolute;top:470px;left:0;width:677px;height:185px;background:var(--green)}
.what-inner{position:absolute;top:18px;left:150px;width:390px;height:150px;border:1px solid rgba(255,255,255,.7)}
.what .section-title{color:var(--white);text-align:center;margin-top:10px}
.services{position:absolute;top:52px;left:48px;display:grid;grid-template-columns:180px 150px;row-gap:14px}
.service{display:flex;align-items:center;gap:8px;color:var(--white);font-size:8px}
.service svg{flex:none}

/* tasks and news */
.tasks{position:absolute;top:680px;left:38px;width:300px}
.tasks .section-title,.news .section-title{font-size:15px}
.tasks-img{margin-top:12px;width:290px;height:110px;background:radial-gradient(circle at 55% 55%,#c8483e 0%,#e7e7e7 35%,#bdbdbd 70%,#f2f2f2 100%)}
.tasks h4{font-size:7px;color:var(--dark);margin-top:8px;font-weight:700}
.tasks ul{list-style:none;margin-top:3px}
.tasks li{position:relative;padding-left:8px;font-size:6.5px;margin-bottom:3px}
.tasks li::before{content:"";position:absolute;left:0;top:3px;width:4px;height:4px;background:var(--green)}
.news{position:absolute;top:680px;left:362px;width:280px}
.news-box{margin-top:12px;background:var(--light);padding:10px 14px;height:225px}
.news-item{display:flex;gap:8px;margin-bottom:10px;background:var(--white);padding:8px}
.news-date{color:var(--green);font-size:6.5px;font-weight:700}
.news-thumb{width:30px;height:30px;flex:none;background:linear-gradient(135deg,#9fb0bd,#d9d9d9)}
.news-item p{font-size:6px;color:var(--text)}
.news-more{display:block;text-align:right;font-size:6px;color:var(--green)}

/* footer */
.site-footer{position:absolute;top:975px;left:0;width:677px;height:195px;background:var(--light);border-top:1px solid var(--mid)}
.footer-col{position:absolute;top:14px;font-size:6.5px;color:var(--text)}
.footer-col h5{font-family:"Cinzel",Georgia,serif;font-size:8px;color:var(--dark);margin-bottom:5px;font-weight:400}
.footer-contact{left:70px;width:160px}
.footer-links{left:270px;width:110px}
.footer-brand{position:absolute;right:40px;top:12px;display:flex;align-items:center;gap:6px}
.footer-brand .brand-square{width:16px;height:16px}
.footer-brand .brand-name{font-size:10px;width:90px}
.newsletter{position:absolute;right:55px;top:90px;width:160px}
.newsletter label{font-size:6.5px;display:block;margin-bottom:4px}
.newsletter .field{height:15px;border:1px solid var(--mid);background:var(--white);font-size:6px;color:var(--grey);padding:3px 5px}
.newsletter .btn{margin-top:5px;margin-left:auto;width:48px;background:var(--green);color:var(--white);font-size:6px;text-align:center;padding:3px 0}
.social{position:absolute;right:55px;top:160px;display:flex;gap:5px}
.social span{width:12px;height:12px;border-radius:50%;background:var(--grey)}
.bottom-bar{position:absolute;top:1170px;left:0;width:677px;height:30px;background:var(--dark);color:#bbbbbb;font-size:6px;text-align:center;line-height:30px}
</style>
</head>
<body>

<header class="site-header">
  <div class="brand"><span class="brand-square"></span><span class="brand-name">Lantern Hill Agency</span></div>
  <div class="client-login">CLIENT LOGIN</div>
  <nav class="main-nav">
    <a class="active" href="#">Home</a>
    <a href="#">About us</a>
    <a href="#">Who we are</a>
    <a href="#">Services</a>
    <a href="#">Contact</a>
    <div class="search">search</div>
  </nav>
</header>

<section class="hero" role="img" aria-label="Panoramic view of a green park along the water with the city skyline behind">
  <div class="hero-caption">Adding the 'where' to your business intelligence enterprise system<br><span class="hero-btn">LEARN MORE</span></div>
  <div class="hero-dots"><span class="on"></span><span></span><span></span><span></span></div>
</section>
<div class="support-tab">SUPPORT</div>

<section class="who">
  <h2 class="section-title">Who we are?</h2>
  <p>Receive high quality professional services from Lantern Hill Agency. Whether your project is large or small, our team of experts can provide the resources and solutions you need to get the job done right. Our track record for consistency, timely service, and subject matter expertise make us a trusted partner for every client.</p>
  <p>Our multifaceted company is here to assist by providing a wide range of services at affordable prices. To speak with an experienced member of staff, simply contact us at your earliest convenience.</p>
</section>

<section class="what">
  <div class="what-inner">
    <h2 class="section-title">What we do?</h2>
    <div class="services">
      <div class="service"><svg width="14" height="14" viewBox="0 0 14 14"><circle cx="7" cy="7" r="6" fill="none" stroke="#fff" stroke-width="1.4"/><circle cx="7" cy="7" r="2" fill="#fff"/></svg>Brand Equity and Positioning</div>
      <div class="service"><svg width="14" height="14" viewBox="0 0 14 14"><rect x="2" y="2" width="10" height="10" fill="none" stroke="#fff" stroke-width="1.4"/><path d="M7 4v6M4 7h6" stroke="#fff" stroke-width="1.4"/></svg>New Product Development</div>
      <div class="service"><svg width="14" height="14" viewBox="0 0 14 14"><path d="M2 12V8M6 12V4M10 12V6" stroke="#fff" stroke-width="2"/></svg>Market Research</div>
      <div class="service"><svg width="14" height="14" viewBox="0 0 14 14"><path d="M3 7l3 3 5-6" fill="none" stroke="#fff" stroke-width="1.6"/></svg>Proprietary Methodologies</div>
      <div class="service"><svg width="14" height="14" viewBox="0 0 14 14"><rect x="1.5" y="3" width="11" height="7" rx="1.5" fill="none" stroke="#fff" stroke-width="1.4"/><path d="M4 10l-1 3 4-3" fill="#fff"/></svg>Communication Services</div>
      <div class="service"><svg width="14" height="14" viewBox="0 0 14 14"><circle cx="5" cy="5" r="2.2" fill="#fff"/><circle cx="10" cy="5" r="2.2" fill="#fff"/><path d="M1 12c0-3 8-3 8 0M6 12c0-3 7-3 7 0" fill="#fff"/></svg>Focus Group Moderation</div>
    </div>
  </div>
</section>

<section class="tasks">
  <h2 class="section-title">Tasks and goals</h2>
  <div class="tasks-img" role="img" aria-label="Archery targets with arrows in the centre"></div>
  <h4>Provision of information</h4>
  <ul>
    <li>about current and fundamental issues related to regional integration, on measures of the Regional Council in the field of higher education</li>
    <li>Suggestions for scientific research and teaching in the field of regional integration</li>
  </ul>
  <h4>Promotion of cooperation between the relevant university associations and the institutions of the Regional Council</h4>
  <h4>Promoting the exchange of views and ideas on integration issues between science and practice</h4>
</section>

<section class="news">
  <h2 class="section-title">Latest News &amp; Events</h2>
  <div class="news-box">
    <div class="news-item"><div class="news-thumb" role="img" aria-label="Event photo"></div><div><div class="news-date">December 18, 2014</div><p>Conference "Lessons and outlook from the regional integration process" held on 16–17 February in the city centre.</p><span class="news-more">read more</span></div></div>
    <div class="news-item"><div class="news-thumb" role="img" aria-label="Event photo"></div><div><div class="news-date">December 18, 2014</div><p>Conference "Lessons and outlook from the regional integration process" held on 16–17 February in the city centre.</p><span class="news-more">read more</span></div></div>
    <div class="news-item"><div class="news-thumb" role="img" aria-label="Event photo"></div><div><div class="news-date">December 18, 2014</div><p>Conference "Lessons and outlook from the regional integration process" held on 16–17 February in the city centre.</p><span class="news-more">read more</span></div></div>
  </div>
</section>

<footer class="site-footer">
  <div class="footer-col footer-contact">
    <h5>Contact us</h5>
    Lantern Hill Agency<br>
    48 Willowmere Green Road<br>
    Brooklyn, NY 11200<br>
    Tel: (555) 014 2288<br>
    hello@lanternhill.example
  </div>
  <div class="footer-col footer-links">
    <h5>Links</h5>
    Who we are<br>About us<br>Services<br>Contact<br>Client login<br>News &amp; events
  </div>
  <div class="footer-brand"><span class="brand-square"></span><span class="brand-name">Lantern Hill Agency</span></div>
  <div class="newsletter">
    <label>Sign in to subscribe newsletter</label>
    <div class="field">enter your email address</div>
    <div class="btn">SUBSCRIBE</div>
  </div>
  <div class="social"><span></span><span></span><span></span></div>
</footer>
<div class="bottom-bar">© 2014 Lantern Hill Agency. All rights reserved.</div>

</body>
</html>
```